Fact Sheets for Insurance

We need a 4 page booklet brochure designed for our insurance business. Each page is A4. We design insurance plans for our Clients and we wish to use the brochure to market and educate our Client and business partners. The business is Halvorsen Brightwick Financial Services. Colour scheme of our logo and stationary is navy blue and metallic gold. The content has been drafted and each page is attached. Please use your creative freedom to make it look professional and modern. We would like graphics, pictures etc to make it more vibrant as well.

Industry/Entity Type

Insurance

```html
<!DOCTYPE html>
<html lang="en">
<head>
<meta charset="utf-8">
<title>Insurance Cheat Sheets – Halvorsen Brightwick Financial Services</title>
<link href="https://fonts.googleapis.com/css2?family=Cinzel:wght@700&family=Arimo:wght@400;700&display=swap" rel="stylesheet">
<style>
  :root{
    --backdrop:#6e6f71;
    --navy:#0f4b6f;
    --navy-deep:#0b3a57;
    --gold:#a8946a;
    --gold-light:#c9b88f;
    --panel:#cdd6e2;
    --paper:#eeece6;
    --ink:#2a2f36;
    --accent-red:#c0392b;
    --number:#7b1f41;
    --white:#ffffff;
  }
  *{box-sizing:border-box;margin:0;padding:0}
  html,body{width:1200px;height:429px;overflow:hidden;background:var(--backdrop)}
  body{font-family:"Arimo",Arial,sans-serif;color:var(--ink)}
  .canvas{position:relative;width:1200px;height:429px;overflow:hidden;
    background:linear-gradient(90deg,#5d5e60,#7a7b7d 50%,#5d5e60)}

  .page{position:absolute;top:4px;width:286px;height:421px;background:var(--paper);overflow:hidden;
    box-shadow:0 0 6px rgba(0,0,0,.35)}
  .page--1{left:8px}.page--2{left:306px}.page--3{left:604px}.page--4{left:902px}
  .page__photo{position:absolute;left:0;right:0;top:80px;bottom:0;
    background:linear-gradient(180deg,rgba(238,236,230,0) 0%,rgba(190,205,218,.55) 55%,rgba(150,172,190,.8) 100%)}
  .page--4 .page__photo{background:linear-gradient(180deg,rgba(238,236,230,0) 0%,rgba(150,185,205,.6) 55%,rgba(70,120,150,.85) 100%)}

  .tab{position:absolute;top:0;width:100px;height:26px;background:var(--gold);color:var(--white);
    font-weight:700;font-size:11.5px;letter-spacing:.3px;display:flex;align-items:center;justify-content:center}
  .brand{position:absolute;top:26px;width:100px;height:46px;background:var(--navy);color:var(--white);
    display:flex;flex-direction:column;align-items:center;justify-content:center;gap:3px;text-align:center}
  .brand__mark{width:9px;height:9px;background:var(--gold-light)}
  .brand__name{font-family:"Cinzel",Georgia,serif;font-size:6.3px;line-height:1.15;color:var(--white)}
  .tab,.brand{left:20px}
  .page--3 .tab,.page--3 .brand,.page--4 .tab,.page--4 .brand{left:166px}

  .title{position:absolute;top:30px;left:128px;width:146px;font-family:"Cinzel",Georgia,serif;
    font-weight:700;font-size:10px;line-height:1.25;color:var(--navy);text-align:right}
  .page--1 .title{color:var(--gold);top:28px}
  .page--3 .title,.page--4 .title{left:20px;text-align:left;width:140px}

  .col{position:absolute;top:88px;width:124px;display:flex;flex-direction:column;gap:4px}
  .col--left{left:20px}.col--right{left:150px}
  .bar{background:var(--navy);color:var(--white);font-weight:700;font-size:7px;text-align:center;padding:4px 2px}
  .page--1 .bar{background:var(--gold)}
  .bar--plain{background:none!important;color:var(--navy);font-size:7.2px;padding:2px;line-height:1.1}
  .page--1 .bar--plain{color:var(--gold)}
  .panel{background:var(--panel);padding:5px 6px;font-size:4.6px;line-height:1.35}
  .panel--clear{background:none}
  .panel p{margin-bottom:3.5px}
  .panel .hl{color:var(--accent-red)}
  .panel .lead{color:var(--navy);font-family:"Cinzel",Georgia,serif;font-weight:700;font-size:5.6px;line-height:1.25}

  .needs{width:100%;border-collapse:collapse;font-size:4.6px}
  .needs th{color:var(--navy);font-weight:700;padding:1px 2px;text-align:left}
  .needs td{padding:1.5px 2px;background:#b9c4d2;border-bottom:1px solid var(--panel)}
  .needs tr.gold td{background:var(--gold-light)}
  .needs tr.total td{font-weight:700;background:none}

  .offers{list-style:none;font-size:5.4px;font-weight:700;color:var(--navy);line-height:1.45}
  .offers li::before{content:"\25B6";font-size:4px;margin-right:4px;color:var(--navy)}
  .page--1 .offers li::before{color:var(--gold)}
  .help{list-style:none;font-size:4.4px;line-height:1.45}
  .help li::before{content:"\25B8";margin-right:3px;color:var(--navy)}

  .callout{background:var(--navy);color:var(--white);padding:10px 6px;font-family:"Cinzel",Georgia,serif;
    font-weight:700;font-size:6.6px;line-height:1.35;text-align:center}
  .page--1 .callout{background:var(--gold)}
  .callout--bare{background:none!important;color:var(--white);padding:8px 2px}
  .callout--gold{color:#e7c35a}

  .disclaimer{position:absolute;left:20px;top:350px;width:250px;height:24px;background:var(--white);
    font-size:3.6px;line-height:1.35;color:#666;padding:4px 6px}
  .footer{position:absolute;left:0;right:0;bottom:0;height:36px}
  .footer--navy{background:var(--navy-deep);color:var(--white)}
  .footer--light{background:var(--white)}
  .footer__num{position:absolute;left:8px;bottom:-2px;font-family:"Cinzel",Georgia,serif;font-weight:700;
    font-size:38px;line-height:1;color:var(--number)}
  .footer__brand{position:absolute;left:50%;top:9px;transform:translateX(-50%);font-family:"Cinzel",Georgia,serif;
    font-size:7px;color:var(--navy);text-align:center;white-space:nowrap}
  .footer__contact{position:absolute;left:132px;top:8px;font-size:3.6px;line-height:1.5;color:var(--white)}
  .footer__name{position:absolute;left:84px;top:10px;font-family:"Cinzel",Georgia,serif;font-size:5px;color:var(--white);width:46px;line-height:1.2}
</style>
</head>
<body>
<main class="canvas">

  <!-- Sheet 1: TPD -->
  <section class="page page--1">
    <div class="page__photo" role="img" aria-label="Faded photograph of a modern office building"></div>
    <div class="tab">CHEAT SHEET</div>
    <div class="brand"><span class="brand__mark"></span><span class="brand__name">Halvorsen Brightwick<br>Financial Services</span></div>
    <h1 class="title">Buying Total and Permanent Disability (TPD) Insurance</h1>
    <div class="col col--left">
      <div class="bar">HOW MUCH DO I NEED?</div>
      <div class="panel">
        <table class="needs">
          <tr><th>NEED</th><th>AMOUNT</th></tr>
          <tr class="gold"><td>Repaying Debts</td><td>$</td></tr>
          <tr><td>Medical Expenses</td><td>$</td></tr>
          <tr class="gold"><td>Home Modification Costs</td><td>$</td></tr>
          <tr><td>Other</td><td>$</td></tr>
          <tr class="total"><td>TOTAL</td><td>$</td></tr>
        </table>
      </div>
      <div class="bar">TIPS &amp; TRAPS</div>
      <div class="panel">
        <p><span class="hl">Purchase an "Own Occupation" definition Policy</span> to ensure that you are not tested against your ability to work "Any Occupation" at claim time.</p>
        <p><span class="hl">Review what the policy doesn't cover "Exclusions".</span> Standard exclusion for most policies is self-inflicted acts.</p>
        <p>Look to <span class="hl">purchase "Long Term" Life Insurance</span> if you think you will need to hold the policy for a number of years. This may save you tens of thousands of dollars over the life of your policy.</p>
        <p>Ensure the contract is <span class="hl">guaranteed to be renewed</span> if you pay your premiums until expiry age.</p>
        <p>If purchased through Super, <span class="hl">you may be liable for a tax bill</span> in the event of a claim</p>
      </div>
    </div>
    <div class="col col--right">
      <div class="bar">WHO OFFERS IT?</div>
      <div class="panel panel--clear">
        <ul class="offers"><li>Most Superannuation Funds</li><li>Some Private Health Funds</li><li>Some Employers</li><li>Life Insurance Companies</li><li>General Insurance Companies</li></ul>
      </div>
      <div class="bar">WHEN TO CALL A PROFESSIONAL ADVISER?</div>
      <div class="panel">
        <p>If you need help:</p>
        <ul class="help"><li>comparing premiums or policies</li><li>reviewing wording of insurance contracts</li><li>matching a policy to suit your occupation purchasing "Long Term" Life Insurance</li><li>purchasing "Long Term" Life Insurance</li></ul>
      </div>
      <div class="callout">If you want to ensure that you have someone assisting your family if a claim is ever needed to be made.</div>
    </div>
    <p class="disclaimer">The information provided on this Fact Sheet is general advice only so does not take into account your objective, financial situation and needs. Before acting on any information contained on this Fact Sheet you should consider the appropriateness of the advice having regard to your own objectives, financial situation and needs.</p>
    <footer class="footer footer--navy">
      <span class="footer__num">1</span>
      <span class="footer__name">Halvorsen Brightwick</span>
      <p class="footer__contact">Suite 4, 18 Harbour Lane, Eastmere<br>T 02 5550 1842 · hello@halvorsenbrightwick.example<br>Authorised representative of a licensed adviser</p>
    </footer>
  </section>

  <!-- Sheet 2: Critical illness -->
  <section class="page page--2">
    <div class="page__photo" role="img" aria-label="Faded photograph of a modern office building"></div>
    <div class="tab">CHEAT SHEET</div>
    <div class="brand"><span class="brand__mark"></span><span class="brand__name">Halvorsen Brightwick<br>Financial Services</span></div>
    <h1 class="title">Buying Critical Illness Insurance</h1>
    <div class="col col--left">
      <div class="bar">HOW MUCH DO I NEED?</div>
      <div class="panel">
        <table class="needs">
          <tr><th>NEED</th><th>AMOUNT</th></tr>
          <tr class="gold"><td>Medical Expenses</td><td>$</td></tr>
          <tr><td>Other</td><td>$</td></tr>
          <tr class="total"><td>TOTAL</td><td>$</td></tr>
        </table>
      </div>
      <div class="bar">TIPS &amp; TRAPS</div>
      <div class="panel">
        <p>Pay particular attention to the definitions for Cancer and Cardiovascular conditions such as Heart Attack so you are aware of when you can claim.</p>
        <p>Review what the policy doesn't cover "Exclusions". Standard exclusion for most policies is self-inflicted acts.</p>
        <p>Look to purchase "Long Term" Life Insurance if you think you will need to hold the policy for a number of years. This may save you tens of thousands of dollars over the life of your policy.</p>
        <p>Ensure the contract is guaranteed to be renewed if you pay your premiums until expiry age.</p>
        <p>Ensure the contract is guaranteed to be renewed if you pay your premiums until expiry age.</p>
      </div>
    </div>
    <div class="col col--right">
      <div class="bar">WHO OFFERS IT?</div>
      <div class="panel">
        <ul class="offers"><li>Some Private Health Funds</li><li>Some Employers</li><li>Life Insurance Companies</li><li>General Insurance Companies</li></ul>
      </div>
      <div class="bar">WHEN TO CALL A PROFESSIONAL ADVISER?</div>
      <div class="panel">
        <p>If you need help:</p>
        <ul class="help"><li>comparing premiums or policies</li><li>reviewing wording of insurance contracts</li><li>purchasing "Long Term" Life Insurance</li></ul>
      </div>
      <div class="callout">If you want to ensure that you have someone assisting you if a claim is ever needed to be made.</div>
    </div>
    <p class="disclaimer">The information provided on this Fact Sheet is general advice only so does not take into account your objective, financial situation and needs. Before acting on any information contained on this Fact Sheet you should consider the appropriateness of the advice having regard to your own objectives, financial situation and needs.</p>
    <footer class="footer footer--light">
      <span class="footer__num">2</span>
      <span class="footer__brand">Halvorsen Brightwick</span>
    </footer>
  </section>

  <!-- Sheet 3: Life insurance -->
  <section class="page page--3">
    <div class="page__photo" role="img" aria-label="Faded photograph of a modern office building"></div>
    <div class="tab">CHEAT SHEET</div>
    <div class="brand"><span class="brand__mark"></span><span class="brand__name">Halvorsen Brightwick<br>Financial Services</span></div>
    <h1 class="title">Buying Life Insurance</h1>
    <div class="col col--left">
      <div class="bar">HOW MUCH DO I NEED?</div>
      <div class="panel">
        <table class="needs">
          <tr><th>NEED</th><th>AMOUNT</th></tr>
          <tr class="gold"><td>Repaying Debts</td><td>$</td></tr>
          <tr><td>Funeral Expenses</td><td>$</td></tr>
          <tr class="gold"><td>Replacing your income</td><td>$</td></tr>
          <tr><td>Other</td><td>$</td></tr>
          <tr class="total"><td>TOTAL</td><td>$</td></tr>
        </table>
      </div>
      <div class="bar">TIPS &amp; TRAPS</div>
      <div class="panel">
        <p>Ensure contract covers all causes of death, not just accidents.</p>
        <p>Review exclusions. The only standard industry exclusion is "suicide within first 13 months of policy inception or reinstatement".</p>
        <p>Look to purchase "Long Term" Life Insurance if you think you will need to hold the policy for a number of years. This may save you tens of thousands of dollars over the life of your policy.</p>
        <p>Ensure the contract is guaranteed to be renewed if you pay your premiums until expiry age.</p>
        <p>If purchased through Super, your beneficiaries may be liable for a tax bill in the event of a claim</p>
      </div>
    </div>
    <div class="col col--right">
      <div class="bar">WHO OFFERS IT?</div>
      <div class="panel">
        <ul class="offers"><li>Most Superannuation Funds</li><li>Some Private Health Funds</li><li>Some Employers</li><li>Life Insurance Companies</li><li>General Insurance Companies</li></ul>
      </div>
      <div class="bar">WHEN TO CALL A PROFESSIONAL ADVISER?</div>
      <div class="panel">
        <ul class="help"><li>comparing premiums or policies</li><li>reviewing wording of policy terms and conditions</li><li>structuring your policies to get a tax deduction</li><li>avoiding tax on any claim proceeds</li><li>purchasing "Long Term" Life Insurance</li></ul>
      </div>
      <div class="callout">If you want to ensure that you have someone assisting your family if a claim is ever needed to be made.</div>
    </div>
    <p class="disclaimer">The information provided on this Fact Sheet is general advice only so does not take into account your objective, financial situation and needs. Before acting on any information contained on this Fact Sheet you should consider the appropriateness of the advice having regard to your own objectives, financial situation and needs.</p>
    <footer class="footer footer--light">
      <span class="footer__num">3</span>
      <span class="footer__brand">Halvorsen Brightwick</span>
    </footer>
  </section>

  <!-- Sheet 4: Income protection -->
  <section class="page page--4">
    <div class="page__photo" role="img" aria-label="Photograph of a waterfront city skyline"></div>
    <div class="tab">CHEAT SHEET</div>
    <div class="brand"><span class="brand__mark"></span><span class="brand__name">Halvorsen Brightwick<br>Financial Services</span></div>
    <h1 class="title">Buying Income Protection Insurance</h1>
    <div class="col col--left">
      <div class="bar">HOW MUCH DO I NEED?</div>
      <div class="panel">
        <p class="lead">Most people insure 75% of their income, which is the maximum benefit that Insurance Companies generally cover.</p>
      </div>
      <div class="bar">TIPS &amp; TRAPS</div>
      <div class="panel">
        <p>Ensure Policy covers all illnesses and injuries, not just accidents.</p>
        <p>Review what the policy doesn't cover "Exclusions". Standard exclusions include self-inflicted acts, pregnancy related illnesses and war related claims.</p>
        <p>Understand the definitions of "Total and Partial Disability" so you know when you can make a claim.</p>
        <p>Look to purchase "Long Term" Life Insurance if you think you will need to hold the policy for a number of years. This may save you tens of thousands of dollars over the life of your policy.</p>
        <p>Ensure the contract is guaranteed to be renewed if you pay your premiums until expiry age.</p>
        <p>Paying the premiums yourself, will generally enable you to claim a tax deduction</p>
      </div>
    </div>
    <div class="col col--right">
      <div class="bar">WHO OFFERS IT?</div>
      <div class="panel panel--clear">
        <ul class="offers"><li>Most Superannuation Funds</li><li>Some Private Health Funds</li><li>Some Employers</li><li>Life Insurance Companies</li><li>General Insurance Companies</li></ul>
      </div>
      <div class="bar bar--plain">WHEN TO CALL A PROFESSIONAL ADVISER?</div>
      <div class="panel panel--clear">
        <p>If you need help:</p>
        <ul class="help"><li>comparing premiums</li><li>reviewing &amp; comparing policy terms and conditions</li><li>matching a policy to suit your occupation</li><li>deciding on the appropriate Waiting Periods and Benefit Periods</li><li>purchasing "Long Term" Life Insurance</li></ul>
      </div>
      <div class="callout callout--bare">If you want to ensure that you have someone assisting you if a claim is ever needed to be made.</div>
      <div class="callout callout--bare callout--gold">If your financial affairs are complex due to being self-employed or a high income earner.</div>
    </div>
    <p class="disclaimer">The information provided on this Fact Sheet is general advice only so does not take into account your objective, financial situation and needs. Before acting on any information contained on this Fact Sheet you should consider the appropriateness of the advice having regard to your own objectives, financial situation and needs.</p>
    <footer class="footer footer--navy">
      <span class="footer__num">4</span>
      <span class="footer__name">Halvorsen Brightwick</span>
      <p class="footer__contact">Suite 4, 18 Harbour Lane, Eastmere<br>T 02 5550 1842 · hello@halvorsenbrightwick.example<br>Authorised representative of a licensed adviser</p>
    </footer>
  </section>

</main>
</body>
</html>
```